Marrowgate Auctions Business Cards Design Needed

I need a business card design that is modern looking - double sided (maybe just my logo on the back, but open to suggestions) - the overall design is up to you. I want it to be easy to read - not over the top flashy. I already have a company logo which I uploaded so that needs to be used. The colors of my logo are the colors I want on the card... so blue and gray (do need to match the logo colors).

Requirements
Must have
• Would like the card to be sleek, modern and easy to ready

```html
<!DOCTYPE html>
<html lang="en">
<head>
<meta charset="utf-8">
<title>Marrowgate Auctions – Business Cards</title>
<link rel="stylesheet" href="https://fonts.googleapis.com/css2?family=Open+Sans:wght@600;700&display=swap">
<style>
  :root {
    --backdrop: #e3170f;
    --brand-blue: #2489c5;
    --brand-gray: #6d7070;
    --ink-gray: #646565;
    --paper: #ffffff;
  }
  html, body {
    margin: 0;
    width: 1200px;
    height: 1200px;
    overflow: hidden;
    background: var(--backdrop);
    font-family: "Open Sans", Arial, sans-serif;
  }
  .card {
    position: absolute;
    width: 1064px;
    height: 590px;
    transform: scale(0.8);
    transform-origin: 0 0;
    background: var(--paper);
    overflow: hidden;
  }
  .card--front { left: 177px; top: 79px; }
  .card--back  { left: 176px; top: 639px; background: var(--brand-gray); }
  .card__shapes { position: absolute; inset: 0; width: 100%; height: 100%; }
  .card__text {
    position: absolute;
    margin: 0;
    font-weight: 600;
    line-height: 1;
    white-space: nowrap;
  }
  .company  { left: 48px; top: 8px; font-size: 42px; color: var(--paper); }
  .person   { left: 48px; top: 72px; font-size: 36px; color: var(--paper); }
  .role     { left: 0; right: 0; top: 150px; text-align: center; font-size: 42px; color: var(--ink-gray); }
  .contact  { left: 0; right: 0; text-align: center; font-size: 40px; color: var(--ink-gray); display: flex; justify-content: center; align-items: center; gap: 10px; }
  .contact--phone { top: 296px; }
  .contact--email { top: 357px; }
  .contact__icon { width: 46px; height: 46px; flex: none; }
  .website  { left: 461px; top: 477px; font-size: 36px; color: var(--paper); }
  .tagline  { left: 0; right: 0; top: 537px; text-align: center; font-size: 40px; color: var(--paper); }
  .wordmark {
    left: 0; right: 0; top: 370px;
    text-align: center;
    font-size: 66px;
    font-weight: 700;
    color: var(--brand-blue);
  }
</style>
</head>
<body>

<section class="card card--front" aria-label="Business card front">
  <svg class="card__shapes" viewBox="0 0 1064 590" aria-hidden="true">
    <polygon points="0,0 1064,0 1064,90 783,90 708,63 0,63" fill="var(--brand-gray)"/>
    <polygon points="0,68 705,68 780,96 1064,96 1064,113 0,113" fill="var(--brand-blue)"/>
    <polygon points="0,477 1064,477 1064,522 355,522 280,496 0,496" fill="var(--brand-blue)"/>
    <polygon points="0,500 278,500 352,526 1064,526 1064,590 0,590" fill="var(--brand-gray)"/>
  </svg>

  <p class="card__text company">Marrowgate Auctions, Inc.</p>
  <p class="card__text person">Owen Carraway</p>
  <p class="card__text role">Owner/President - Auctioneer</p>

  <p class="card__text contact contact--phone">
    <svg class="contact__icon" viewBox="0 0 46 46" aria-hidden="true">
      <circle cx="23" cy="23" r="20" fill="none" stroke="var(--ink-gray)" stroke-width="3"/>
      <path d="M15 13c2-2 4-1 5 1l2 4c1 2 0 3-1 4l-1 1c1 3 3 5 6 6l1-1c1-1 2-2 4-1l4 2c2 1 3 3 1 5-2 2-4 3-7 2-6-2-12-8-14-14-1-3 0-6 0-9z" fill="var(--ink-gray)"/>
    </svg>
    702-555-0148
  </p>
  <p class="card__text contact contact--email">
    <svg class="contact__icon" viewBox="0 0 46 46" aria-hidden="true">
      <circle cx="23" cy="23" r="20" fill="none" stroke="var(--ink-gray)" stroke-width="3"/>
      <rect x="11" y="15" width="22" height="15" rx="1" fill="var(--ink-gray)"/>
      <polyline points="11,16 22,24 33,16" fill="none" stroke="var(--paper)" stroke-width="2"/>
    </svg>
    owen@marrowgate.com
  </p>

  <p class="card__text website">http://bidrevival.com</p>
  <p class="card__text tagline">Improving Charity Auctions Nationwide</p>
</section>

<section class="card card--back" aria-label="Business card back">
  <svg class="card__shapes" viewBox="0 0 1062 590" aria-hidden="true">
    <polygon points="385,0 680,0 985,413 770,590 310,590 75,413" fill="var(--paper)"/>
    <polygon points="407,0 660,0 965,413 750,590 330,590 95,413" fill="var(--brand-blue)"/>
    <polygon points="433,0 628,0 930,413 690,590 370,590 130,413" fill="var(--paper)"/>
  </svg>
  <p class="card__text wordmark">Marrowgate Auctions</p>
</section>

</body>
</html>
```